Brimovex business card

Based on company logo and website given , to design a business card temple. Slogan "Care your pets can always count on"
Color style please refer to our website

```html
<!DOCTYPE html>
<html lang="en">
<head>
<meta charset="utf-8">
<title>Brimovex stationery</title>
<link href="https://fonts.googleapis.com/css2?family=Barlow+Semi+Condensed:wght@500;600&family=Nunito+Sans:wght@400;600&display=swap" rel="stylesheet">
<style>
  :root {
    --brand-blue: #0a69b3;
    --brand-gold: #c7ad31;
    --ink: #4a4a4a;
    --ink-soft: #777;
    --paper: #ffffff;
    --backdrop: #f1f1f1;
    --edge: #cfcfcf;
  }
  * { box-sizing: border-box; margin: 0; padding: 0; }
  html, body { width: 946px; height: 1200px; overflow: hidden; background: var(--backdrop); }
  body { position: relative; font-family: "Nunito Sans", sans-serif; color: var(--ink); }

  .letterhead {
    position: absolute; left: 47px; top: 42px; width: 765px; height: 1082px;
    background: var(--paper); border: 1px solid var(--edge); overflow: hidden;
  }
  .letterhead > * { position: absolute; }
  .bar { left: 90px; width: 238px; height: 12px; }
  .bar-top { top: 0; background: var(--brand-blue); }
  .bar-bottom { bottom: 0; background: var(--brand-gold); }

  .wordmark {
    font-family: "Barlow Semi Condensed", sans-serif; font-weight: 600;
    color: var(--brand-blue); line-height: 1;
  }
  .tagline { color: var(--brand-gold); font-family: "Nunito Sans", sans-serif; white-space: nowrap; }

  .letter-logo { left: 84px; top: 62px; width: 250px; text-align: center; }
  .letter-logo .wordmark { font-size: 66px; }
  .letter-logo .tagline { font-size: 14px; margin-top: 2px; }

  .heading {
    font-family: "Barlow Semi Condensed", sans-serif; font-weight: 600;
    color: var(--brand-gold); font-size: 18px; line-height: 1;
  }
  .recipient { left: 454px; top: 154px; }
  .recipient ul { list-style: none; margin-top: 6px; font-size: 13px; line-height: 18px; }
  .date { left: 454px; top: 266px; }
  .subject { left: 90px; top: 319px; }

  .letter-body { left: 90px; top: 358px; width: 585px; font-size: 13.2px; line-height: 18px; }
  .letter-body p { margin-bottom: 18px; }

  .sign-off { left: 90px; top: 776px; font-size: 13.2px; }
  .signature { left: 311px; top: 793px; width: 144px; height: 58px;
    background: linear-gradient(90deg, #e9e9e9, #d8d8d8); border-radius: 4px; }
  .signatory { left: 280px; top: 850px; width: 210px; text-align: center; }
  .signatory .name { font-family: "Barlow Semi Condensed", sans-serif; font-weight: 600; font-size: 18px; color: #555; }
  .signatory .role { font-size: 9px; letter-spacing: 5px; color: #555; margin-top: 1px; }

  .letter-contacts { left: 100px; top: 966px; list-style: none; font-family: "Barlow Semi Condensed", sans-serif; font-size: 10.5px; color: var(--ink-soft); }
  .letter-contacts li { display: flex; align-items: center; gap: 10px; height: 25px; }
  .letter-contacts svg { width: 12px; height: 12px; fill: none; stroke: var(--brand-gold); stroke-width: 2; }

  .card { position: absolute; left: 580px; width: 340px; height: 201px; border: 1px solid var(--edge); overflow: hidden; }
  .card-back { top: 441px; background: var(--paper); }
  .card-back .logo-zone { position: absolute; left: 0; top: 0; width: 186px; height: 108px; text-align: center; padding-top: 26px; }
  .card-back .wordmark { font-size: 32px; }
  .card-back .tagline { font-size: 6.5px; margin-top: 3px; }
  .card-back .name-panel {
    position: absolute; left: 0; top: 108px; width: 182px; height: 93px;
    background: var(--brand-gold); color: #fff; text-align: center; padding-top: 28px;
  }
  .name-panel .name { font-family: "Barlow Semi Condensed", sans-serif; font-weight: 600; font-size: 18px; line-height: 1; }
  .name-panel .role { font-size: 9px; letter-spacing: 6px; font-weight: 600; margin-top: 3px; }
  .card-back .contact-panel {
    position: absolute; left: 186px; top: 0; width: 154px; height: 201px;
    background: var(--brand-blue); color: #fff; padding: 112px 0 0 10px;
    font-family: "Barlow Semi Condensed", sans-serif; font-size: 10px; line-height: 12.4px;
  }
  .contact-panel ul { list-style: none; }
  .contact-panel li { display: flex; gap: 8px; }
  .contact-panel svg { width: 9px; height: 9px; flex: none; margin-top: 2px; fill: none; stroke: #fff; stroke-width: 2; }

  .card-front { top: 695px; background: var(--brand-blue); text-align: center; padding-top: 66px; }
  .card-front .wordmark { color: #fff; font-size: 52px; }
  .card-front .tagline { font-size: 11px; margin-top: 8px; }
</style>
</head>
<body>
  <section class="letterhead">
    <div class="bar bar-top"></div>
    <div class="letter-logo">
      <div class="wordmark">Brimovex</div>
      <div class="tagline">Care your pets can always count on</div>
    </div>

    <div class="recipient">
      <div class="heading">Companies</div>
      <ul>
        <li>- Mr / Ms contact person</li>
        <li>- Street, PO Box</li>
        <li>- Postcode / town</li>
      </ul>
    </div>
    <div class="heading date">Date</div>
    <div class="heading subject">Subject / reference</div>

    <div class="letter-body">
      <p>Salutation of the contact person</p>
      <p>Lorem ipsum dolor sit amet, consectetuer adipiscing elit, sed diam nonummy nibh euismod tincidunt ut laoreet dolore magna aliquam erat volutpat. Ut wisi enim ad minim veniam, quis nostrud exerci tation ullamcorper suscipit lobortis nisl ut aliquip ex ea commodo consequat. Duis autem vel eum iriure dolor in hendrerit in vulputate velit esse molestie consequat, vel illum dolore eu feugiat nulla facilisis at vero eros et accumsan et iusto odio dignissim qui blandit praesent luptatum zzril delenit augue duis dolore te feugait nulla facilisi.</p>
      <p>Lorem ipsum dolor sit amet, cons ectetuer adipiscing elit, sed diam nonummy nibh euismod tincidunt ut laoreet dolore magna aliquam erat volutpat. Ut wisi enim ad minim veniam, quis nostrud exerci tation ullamcorper suscipit lobortis nisl ut aliquip ex ea commodo consequat. Lorem ipsum dolor sit amet, consectetuer adipiscing elit, sed diam nonummy nibh euismod tincidunt ut laoreet dolore magna aliquam erat volutpat. Ut wisi enim ad minim veniam, quis nostrud exerci tation ullamcorper suscipit lobortis nisl ut aliquip ex ea commodo consequat.</p>
      <p>Duis autem vel eum iriure dolor in hendrerit in vulputate velit esse molestie consequat, vel illum dolore eu feugiat nulla facilisis at vero eros et accumsan et iusto odio dignissim qui blandit praesent luptatum zzril delenit augue duis dolore te feugait nulla facilisi.<br>Lorem ipsum dolor sit amet, cons ectetuer adipiscing elit, sed diam nonummy nibh euismod tincidunt ut laoreet dolore magna aliquam erat volutpat. Ut wisi enim ad minim veniam, quis nostrud exerci tation ullamcorper suscipit lobortis nisl ut aliquip ex ea commodo consequat.</p>
    </div>

    <div class="sign-off">With best regards,</div>
    <div class="signature" role="img" aria-label="Handwritten signature"></div>
    <div class="signatory">
      <div class="name">Name Surname</div>
      <div class="role">OWNER</div>
    </div>

    <ul class="letter-contacts">
      <li><svg viewBox="0 0 12 12"><path d="M6 11 C3 7 2 5.5 2 4.2 A4 4 0 0 1 10 4.2 C10 5.5 9 7 6 11Z"/><circle cx="6" cy="4.3" r="1.2"/></svg>12/40 Harlow Street, Glen Ashby Vic 3188</li>
      <li><svg viewBox="0 0 12 12"><path d="M2 2 L4.5 1.5 L5.5 4 L4 5 C4.8 6.8 5.5 7.5 7 8 L8 6.5 L10.5 7.5 L10 10 C5.5 10 2 6.5 2 2Z"/></svg>+61 3 7410 2286 &nbsp;|&nbsp; 1800 330 417</li>
      <li><svg viewBox="0 0 12 12"><rect x="1" y="2.5" width="10" height="7"/><path d="M1 2.5 L6 6.5 L11 2.5"/></svg>sales@brimovex.com.au</li>
      <li><svg viewBox="0 0 12 12"><circle cx="6" cy="6" r="5"/><circle cx="6" cy="5" r="1.7"/><path d="M3 9.5 C4.5 7.5 7.5 7.5 9 9.5"/></svg>www.brimovex.com.au</li>
    </ul>
    <div class="bar bar-bottom"></div>
  </section>

  <section class="card card-back">
    <div class="logo-zone">
      <div class="wordmark">Brimovex</div>
      <div class="tagline">Care your pets can always count on</div>
    </div>
    <div class="name-panel">
      <div class="name">Name Surname</div>
      <div class="role">TITLE</div>
    </div>
    <div class="contact-panel">
      <ul>
        <li><svg viewBox="0 0 12 12"><path d="M6 11 C3 7 2 5.5 2 4.2 A4 4 0 0 1 10 4.2 C10 5.5 9 7 6 11Z"/><circle cx="6" cy="4.3" r="1.2"/></svg><span>12/40 Harlow Street<br>Glen Ashby Vic 3188</span></li>
        <li><svg viewBox="0 0 12 12"><path d="M2 2 L4.5 1.5 L5.5 4 L4 5 C4.8 6.8 5.5 7.5 7 8 L8 6.5 L10.5 7.5 L10 10 C5.5 10 2 6.5 2 2Z"/></svg><span>+61 3 7410 2286<br>1800 330 417</span></li>
        <li><svg viewBox="0 0 12 12"><rect x="1" y="2.5" width="10" height="7"/><path d="M1 2.5 L6 6.5 L11 2.5"/></svg><span>sales@brimovex.com.au</span></li>
        <li><svg viewBox="0 0 12 12"><circle cx="6" cy="6" r="5"/><circle cx="6" cy="5" r="1.7"/><path d="M3 9.5 C4.5 7.5 7.5 7.5 9 9.5"/></svg><span>www.brimovex.com.au</span></li>
      </ul>
    </div>
  </section>

  <section class="card card-front">
    <div class="wordmark">Brimovex</div>
    <div class="tagline">Care your pets can always count on</div>
  </section>
</body>
</html>
```